Pellu an Organic Supplement Brand

A product label for a Supplement Brand. Company is called "Pellu" and the tagline is "Wellness Grown Together". Their will be multiple products such as capsules, liquids, powders, etc. Lets focus on Vitamin C capsules, but if you want to play around with color pallets and or multiple supplements that would be great. Want it to be a simple, clean and sophisticated design that looks fresh and stands out. This product has high quality organic ingredients. Attached is label specifications as well as an image for stock language for left and right side of label for reference and some sample products. Parts can be omitted, added or mixed and matched as needed.
Moms
Health and Wellness

```html
<!DOCTYPE html>
<html lang="en">
<head>
<meta charset="UTF-8">
<title>Pellu Vitamin C Label</title>
<link rel="stylesheet" href="https://fonts.googleapis.com/css2?family=Raleway:wght@300&family=Open+Sans:ital,wght@1,700&family=Poppins:wght@600&family=Montserrat:wght@500;700&display=swap">
<style>
  :root {
    --backdrop: #e2e3e4;
    --label: #ffffff;
    --sun: #f2c11d;
    --sun-light: #fad95a;
    --sun-deep: #e3a813;
    --ink: #2f2f2f;
    --white: #ffffff;
  }
  * { margin: 0; padding: 0; box-sizing: border-box; }
  html, body {
    width: 1200px; height: 1200px; overflow: hidden;
    background: var(--backdrop);
  }
  .label {
    position: absolute; left: 90px; top: 5px;
    width: 1020px; height: 1190px;
    background: var(--label);
    overflow: hidden;
  }
  .label svg.bands { position: absolute; inset: 0; }
  .brand {
    position: absolute; left: 0; right: 0; top: 38px;
    text-align: center;
    font-family: "Raleway", sans-serif; font-weight: 300;
    font-size: 86px; letter-spacing: 0.04em; line-height: 1;
    color: var(--white);
  }
  .tagline {
    position: absolute; left: 0; right: 0; top: 130px;
    text-align: center;
    font-family: "Open Sans", sans-serif; font-style: italic; font-weight: 700;
    font-size: 27px; color: var(--white); line-height: 1;
  }
  .product-name {
    position: absolute; left: 0; right: 0; top: 478px;
    text-align: center;
    font-family: "Poppins", sans-serif; font-weight: 600;
    font-size: 146px; line-height: 1; letter-spacing: -0.005em;
    color: var(--ink);
  }
  .product-type {
    position: absolute; left: 0; right: 0; top: 630px;
    text-align: center;
    font-family: "Montserrat", sans-serif; font-weight: 700;
    font-size: 38px; letter-spacing: 0.13em; line-height: 1;
    color: var(--sun);
  }
  .count-badge {
    position: absolute; left: 136px; top: 961px;
    width: 222px; height: 170px;
    background: var(--sun); border-radius: 16px;
    border: 4px solid var(--sun-light);
  }
  .count-badge svg { position: absolute; left: 14px; top: 20px; }
  .count-number {
    position: absolute; left: 74px; top: 16px;
    font-family: "Montserrat", sans-serif; font-weight: 700;
    font-size: 64px; line-height: 1; color: var(--white);
  }
  .count-unit {
    position: absolute; left: 74px; top: 84px;
    font-family: "Montserrat", sans-serif; font-weight: 500;
    font-size: 18px; line-height: 1; color: var(--white);
  }
  .count-dose {
    position: absolute; left: 0; right: 0; top: 120px;
    text-align: center;
    font-family: "Montserrat", sans-serif; font-weight: 500;
    font-size: 30px; letter-spacing: 0.05em; line-height: 1; color: var(--white);
  }
  .capsule-type {
    position: absolute; left: 413px; top: 1040px;
    font-family: "Montserrat", sans-serif; font-weight: 500;
    font-size: 31px; letter-spacing: 0.15em; line-height: 1;
    color: var(--white);
  }
</style>
</head>
<body>
  <main class="label">
    <svg class="bands" width="1020" height="1190" viewBox="0 0 1020 1190" aria-hidden="true">
      <defs>
        <linearGradient id="sunband" x1="0" y1="0" x2="0" y2="1">
          <stop offset="0" stop-color="#f3c624"/>
          <stop offset="1" stop-color="#efb915"/>
        </linearGradient>
      </defs>
      <path d="M0 0 H1020 V160 C780 230 560 258 330 240 C200 230 90 200 0 180 Z" fill="var(--sun-deep)" opacity="0.55"/>
      <path d="M0 0 H1020 V140 C780 215 560 240 330 222 C200 212 90 190 0 170 Z" fill="url(#sunband)"/>
      <rect x="0" y="995" width="1020" height="8" fill="var(--sun-light)"/>
      <rect x="0" y="1003" width="1020" height="94" fill="var(--sun)"/>
    </svg>

    <div class="brand">PELLU</div>
    <div class="tagline">Wellness Grown Together</div>

    <h1 class="product-name">Vitamin C</h1>
    <div class="product-type">DIETARY SUPPLEMENT</div>

    <div class="count-badge">
      <svg width="48" height="84" viewBox="0 0 48 84" aria-hidden="true">
        <rect x="3" y="3" width="42" height="78" rx="21" fill="none" stroke="var(--white)" stroke-width="5"/>
        <path d="M3 42 V24 A21 21 0 0 1 45 24 V42 Z" fill="var(--white)"/>
      </svg>
      <div class="count-number">180</div>
      <div class="count-unit">CAPSULES</div>
      <div class="count-dose">500 MG</div>
    </div>
    <div class="capsule-type">VEGETARIAN CAPSULES</div>
  </main>
</body>
</html>
```